Innovative Veterinary Clinic Business Card

We are a mixed animal veterinary practice in rural Queensland. Our patients include cattle, horses, dogs and cats, with everything in between. We are moving the clinic forward to become the best in our region and one of the best in the State, with gold standard service and standards of care, while remaining down to earth and genuine. Our current motto is - "The difference is, we care". The clinic colours are blue and red but am open to change. I would like something innovative and modern, that stands out and says we are different, we are amazing, and our patients come first. Something that will be remembered. Our current logo and business card I feel are empty and don't stand out.
Updates

please use font that is strong but simple. I am looking for something different, rather than your run of the mill business card. I am open to anything - as long as it has two sides and defines us, I'll consider all submissions. Thank you for your efforts, they are all very much appreciated!!

Thank you all very much for your amazing efforts. I wasn't expecting to have such a great response, so I thank you for your participation. You are all very talented and I loved your designs. I wish you all the best for the future. Thank you!

Target Market(s)

pet owners, graziers, horse clients (horses of all types - pets, campdrafting, mustering, polocrosse, thoroughbreds, show ponies)

Industry/Entity Type

Veterinary

Contact Information for Business Card

Dr. Petra L Hovland - BVSc (Hons)
Greenhollow Veterinary Services
18 Carrow St
Kelwarra, QLD, 4619
Ph: 0746382117 or 0418273946
Fax: 0746382110
e: greenhollowvet@mailbrook.net

Colors

Designer to choose colors to be used in the design.

Requirements
Must have
• back side of card to be used as an appointment card
Nice to have
• perhaps a photo of an animal (horse, dog, cat, cattle)
Should not have
• I don't want the standard name, rank and serial number business card. No cartoon animals.

```html
<!DOCTYPE html>
<html lang="en">
<head>
<meta charset="utf-8">
<title>Greenhollow Veterinary Services – Business Card</title>
<link rel="stylesheet" href="https://fonts.googleapis.com/css2?family=Questrial&family=Arimo:wght@400&display=swap">
<style>
  :root {
    --page-bg: #d4d4d4;
    --card-dark: #231f20;
    --white: #ffffff;
    --ink: #111111;
    --navy: #2a2462;
    --photo-light: #eef1f2;
    --photo-mist: #e3e8ea;
    --photo-fur: #e7b690;
    --photo-deep: #c98a5c;
    --photo-shadow: #6f5a63;
    --icon-fill: #8a8788;
  }
  * { box-sizing: border-box; margin: 0; padding: 0; }
  html, body { width: 1000px; height: 1200px; overflow: hidden; }
  body { background: var(--page-bg); position: relative; font-family: "Arimo", Arial, sans-serif; }

  .card { position: absolute; overflow: hidden; }

  /* Front */
  .card--front { left: 200px; top: 162px; width: 625px; height: 379px; }
  .card__photo {
    position: absolute; inset: 0;
    background:
      radial-gradient(ellipse 45% 60% at 72% 45%, var(--photo-fur) 0%, var(--photo-deep) 55%, transparent 100%),
      linear-gradient(90deg, var(--photo-light) 0%, var(--photo-mist) 35%, #f0e0d2 55%, var(--photo-deep) 80%, var(--photo-shadow) 100%);
  }
  .doctor { position: absolute; left: 36px; top: 71px; color: var(--navy); }
  .doctor__name { font-family: "Questrial", "Century Gothic", sans-serif; font-size: 21px; line-height: 24px; letter-spacing: 0.2px; }
  .doctor__degree { font-size: 13px; line-height: 17px; margin-top: 1px; }
  .practice { position: absolute; left: 36px; top: 255px; color: var(--ink); }
  .practice__name { font-size: 15px; line-height: 18px; margin-bottom: 4px; }
  .practice__line { font-size: 11px; line-height: 15px; }

  /* Back */
  .card--back { left: 186px; top: 669px; width: 647px; height: 385px; background: var(--card-dark); color: var(--white); }
  .species__row { position: absolute; left: 45px; width: 110px; height: 64px; }
  .species__row--dog { top: 34px; }
  .species__row--cat { top: 118px; }
  .species__row--horse { top: 202px; }
  .species__row--cow { top: 286px; }
  .species__badge { position: absolute; left: 0; top: 0; width: 64px; height: 64px; }
  .species__check { position: absolute; left: 83px; top: 17px; width: 23px; height: 23px; background: var(--white); }
  .species__row--cat .species__check { top: 21px; }
  .species__row--cow .species__check { top: 22px; }
  .species__check svg { position: absolute; left: 0; top: -4px; }

  .appointment__label {
    position: absolute; left: 269px; top: 179px;
    font-family: "Questrial", "Century Gothic", sans-serif; font-size: 18px; letter-spacing: 0.5px;
    transform: translate(-50%, -50%) rotate(-90deg); white-space: nowrap;
  }
  .field-label { position: absolute; font-family: "Questrial", "Century Gothic", sans-serif; font-size: 15px; transform: translateX(-50%); }
  .field-label--date { left: 360px; top: 94px; }
  .field-label--time { left: 516px; top: 92px; }
  .field { position: absolute; background: var(--white); }
  .field--date { left: 286px; top: 118px; width: 154px; height: 28px; }
  .field--time { left: 446px; top: 118px; width: 153px; height: 28px; }
  .field--notes { left: 286px; top: 153px; width: 313px; height: 89px; }
  .appointment__note { position: absolute; right: 46px; top: 261px; text-align: right; font-size: 12px; line-height: 20px; white-space: nowrap; }
</style>
</head>
<body>

<section class="card card--front">
  <div class="card__photo" role="img" aria-label="Photo of a ginger kitten with its mouth open, fading to a soft pale background on the left"></div>
  <div class="doctor">
    <p class="doctor__name">Dr. Petra L Hovland</p>
    <p class="doctor__degree">BVSc (Hons)</p>
  </div>
  <div class="practice">
    <p class="practice__name">Greenhollow Veterinary Services</p>
    <p class="practice__line">18 Carrow St Kelwarra, QLD, 4619</p>
    <p class="practice__line">Ph: 0746382117 / 0418273946</p>
    <p class="practice__line">Fax: 0746382110</p>
    <p class="practice__line">Email: greenhollowvet@mailbrook.net</p>
  </div>
</section>

<section class="card card--back">
  <div class="species">
    <div class="species__row species__row--dog">
      <svg class="species__badge" viewBox="0 0 64 64"><circle cx="32" cy="32" r="29" fill="none" stroke="var(--white)" stroke-width="4"/><circle cx="32" cy="32" r="20" fill="var(--icon-fill)" role="img" aria-label="Dog silhouette icon"/></svg>
      <span class="species__check"></span>
    </div>
    <div class="species__row species__row--cat">
      <svg class="species__badge" viewBox="0 0 64 64"><circle cx="32" cy="32" r="29" fill="none" stroke="var(--white)" stroke-width="4"/><circle cx="32" cy="32" r="20" fill="var(--icon-fill)" role="img" aria-label="Cat silhouette icon"/></svg>
      <span class="species__check"></span>
    </div>
    <div class="species__row species__row--horse">
      <svg class="species__badge" viewBox="0 0 64 64"><circle cx="32" cy="32" r="29" fill="none" stroke="var(--white)" stroke-width="4"/><circle cx="32" cy="32" r="20" fill="var(--icon-fill)" role="img" aria-label="Horse silhouette icon"/></svg>
      <span class="species__check"><svg width="26" height="28" viewBox="0 0 26 28"><path d="M4 17 L10 24 L23 3" fill="none" stroke="var(--ink)" stroke-width="2.5"/></svg></span>
    </div>
    <div class="species__row species__row--cow">
      <svg class="species__badge" viewBox="0 0 64 64"><circle cx="32" cy="32" r="29" fill="none" stroke="var(--white)" stroke-width="4"/><circle cx="32" cy="32" r="20" fill="var(--icon-fill)" role="img" aria-label="Cow silhouette icon"/></svg>
      <span class="species__check"></span>
    </div>
  </div>

  <p class="appointment__label">Appoinment</p>
  <p class="field-label field-label--date">Date</p>
  <p class="field-label field-label--time">Time</p>
  <div class="field field--date"></div>
  <div class="field field--time"></div>
  <div class="field field--notes"></div>
  <p class="appointment__note">if you are unable to attend this appointment,<br>please give us a call as soon as possible</p>
</section>

</body>
</html>
```